依頼詳細
当店一品料理での一番人気商品「炭焼き月白鶏」を常温仕様で作成し、通信販売、ギフト等に活用できるようにと思います。
記載項目
サイズ 縦12cm×横20cm×高さ3cmの半透明のプラスチック箱の内側にミラー紙180kの紙を差込みます。(紙は縦15cm×横20cmで縦15cmの上部3cmは上面に折ります。
その紙のデザインを希望いたします。
文字は (一味ちがう  「炭焼き月白鶏」)と(店のロゴ)を入れる予定です。
オリーブを連想できるような色を希望いたします。
希望イメージ
シンプル 複雑
単色 カラフル
暗い 明るい
日常 高級
遊び心 厳粛
未来的 伝統的
女性的 男性的
希望する色
緑系
納品ファイル
• 高解像度JPG (.jpg)
補足説明
■ 選んだ理由

思いつかないような素晴らしいデザインで有難うございました。とても満足致しております。
今後とも何卒宜しくお願い致します。

■ 提案者全員のお礼・コメント

お忙しい中数多くのご提案を頂きまして有難うございました。
今後とも何卒宜しくお願い致します。

```html
<!DOCTYPE html>
<html lang="ja">
<head>
<meta charset="utf-8">
<title>炭焼き月白鶏 パッケージ差込紙</title>
<link rel="stylesheet" href="https://fonts.googleapis.com/css2?family=Noto+Sans+JP:wght@500;900&display=swap">
<style>
  :root {
    --canvas: #ffffff;
    --panel-dark: #1f2a1c;
    --panel-mid: #2c3a26;
    --gold: #c9a64a;
    --gold-light: #e8d08a;
    --olive: #9aac4f;
    --olive-deep: #6f8131;
    --label-olive: #9bb04e;
    --label-cream: #fbf8ee;
    --ink: #141414;
    --leaf-tone: #4d5d2a;
  }
  html, body {
    margin: 0;
    padding: 0;
    width: 783px;
    height: 1200px;
    overflow: hidden;
    background: var(--canvas);
  }
  .sheet {
    position: relative;
    width: 783px;
    height: 1200px;
    font-family: "Noto Sans JP", sans-serif;
  }
  .variant {
    position: absolute;
    left: 0;
    width: 783px;
    height: 540px;
    display: block;
  }
  .variant--olive { top: 12px; }
  .variant--cream { top: 630px; }
  .label-name { font-weight: 900; font-size: 60px; fill: var(--ink); }
  .label-tagline { font-weight: 500; font-size: 22px; fill: var(--ink); letter-spacing: 2px; }
  .band-tagline { font-weight: 500; font-size: 20px; fill: var(--ink); }
  .band-name { font-weight: 900; font-size: 50px; fill: var(--ink); }
</style>
</head>
<body>
<main class="sheet">

  <!-- Variant A: olive label -->
  <svg class="variant variant--olive" viewBox="0 0 783 540" xmlns="http://www.w3.org/2000/svg">
    <defs>
      <radialGradient id="panelGlowA" cx="50%" cy="45%" r="70%">
        <stop offset="0" stop-color="#33432b"/>
        <stop offset="1" stop-color="#1a2317"/>
      </radialGradient>
      <linearGradient id="labelOlive" x1="0" y1="0" x2="0" y2="1">
        <stop offset="0" stop-color="#b2c562"/>
        <stop offset="1" stop-color="#86993c"/>
      </linearGradient>
      <linearGradient id="goldLine" x1="0" y1="0" x2="1" y2="1">
        <stop offset="0" stop-color="#e8d08a"/>
        <stop offset="0.5" stop-color="#b8902f"/>
        <stop offset="1" stop-color="#e8d08a"/>
      </linearGradient>
    </defs>
    <rect class="panel" role="img" aria-label="olive leaf pattern on dark green" x="14" y="0" width="755" height="452" fill="url(#panelGlowA)"/>
    <path class="frame-outer" d="M70 30 H713 A30 30 0 0 0 743 60 V392 A30 30 0 0 0 713 422 H70 A30 30 0 0 0 40 392 V60 A30 30 0 0 0 70 30 Z" fill="none" stroke="url(#goldLine)" stroke-width="3"/>
    <path class="frame-inner" d="M78 44 H705 A22 22 0 0 0 727 66 V386 A22 22 0 0 0 705 408 H78 A22 22 0 0 0 56 386 V66 A22 22 0 0 0 78 44 Z" fill="none" stroke="url(#goldLine)" stroke-width="1.5"/>
    <g class="label">
      <rect x="185" y="140" width="413" height="160" rx="26" fill="var(--label-cream)"/>
      <rect x="193" y="148" width="397" height="144" rx="20" fill="url(#labelOlive)" stroke="var(--gold)" stroke-width="2"/>
      <path d="M371 140 q20 -22 40 0" fill="none" stroke="var(--label-cream)" stroke-width="4"/>
      <text class="label-name" x="391.5" y="232" text-anchor="middle">炭焼き月白鶏</text>
      <text class="label-tagline" x="391.5" y="272" text-anchor="middle">一味ちがう</text>
    </g>
    <rect class="band" x="0" y="448" width="783" height="78" fill="var(--olive)"/>
    <line x1="0" y1="452" x2="783" y2="452" stroke="var(--gold)" stroke-width="2"/>
    <line x1="0" y1="522" x2="783" y2="522" stroke="var(--gold)" stroke-width="2"/>
    <rect role="img" aria-label="olive sprig" x="22" y="466" width="60" height="42" rx="21" fill="var(--leaf-tone)"/>
    <rect role="img" aria-label="olive sprig" x="701" y="466" width="60" height="42" rx="21" fill="var(--leaf-tone)"/>
    <text class="band-tagline" x="110" y="500">一味ちがう</text>
    <text class="band-name" x="250" y="506">炭焼き月白鶏</text>
  </svg>

  <!-- Variant B: cream label -->
  <svg class="variant variant--cream" viewBox="0 0 783 540" xmlns="http://www.w3.org/2000/svg">
    <defs>
      <radialGradient id="panelGlowB" cx="50%" cy="45%" r="70%">
        <stop offset="0" stop-color="#33432b"/>
        <stop offset="1" stop-color="#1a2317"/>
      </radialGradient>
      <linearGradient id="goldLineB" x1="0" y1="0" x2="1" y2="1">
        <stop offset="0" stop-color="#e8d08a"/>
        <stop offset="0.5" stop-color="#b8902f"/>
        <stop offset="1" stop-color="#e8d08a"/>
      </linearGradient>
    </defs>
    <rect class="panel" role="img" aria-label="olive leaf pattern on dark green" x="14" y="0" width="755" height="452" fill="url(#panelGlowB)"/>
    <path class="frame-outer" d="M70 30 H713 A30 30 0 0 0 743 60 V392 A30 30 0 0 0 713 422 H70 A30 30 0 0 0 40 392 V60 A30 30 0 0 0 70 30 Z" fill="none" stroke="url(#goldLineB)" stroke-width="3"/>
    <path class="frame-inner" d="M78 44 H705 A22 22 0 0 0 727 66 V386 A22 22 0 0 0 705 408 H78 A22 22 0 0 0 56 386 V66 A22 22 0 0 0 78 44 Z" fill="none" stroke="url(#goldLineB)" stroke-width="1.5"/>
    <g class="label">
      <rect x="185" y="140" width="413" height="160" rx="26" fill="var(--gold)"/>
      <rect x="191" y="146" width="401" height="148" rx="21" fill="var(--label-cream)" stroke="var(--gold-light)" stroke-width="2"/>
      <path d="M371 140 q20 -22 40 0" fill="none" stroke="var(--gold)" stroke-width="4"/>
      <text class="label-name" x="391.5" y="232" text-anchor="middle">炭焼き月白鶏</text>
      <text class="label-tagline" x="391.5" y="272" text-anchor="middle">一味ちがう</text>
    </g>
    <rect class="band" x="0" y="448" width="783" height="78" fill="var(--olive)"/>
    <line x1="0" y1="452" x2="783" y2="452" stroke="var(--gold)" stroke-width="2"/>
    <line x1="0" y1="522" x2="783" y2="522" stroke="var(--gold)" stroke-width="2"/>
    <rect role="img" aria-label="olive sprig" x="22" y="466" width="60" height="42" rx="21" fill="var(--leaf-tone)"/>
    <rect role="img" aria-label="olive sprig" x="701" y="466" width="60" height="42" rx="21" fill="var(--leaf-tone)"/>
    <text class="band-tagline" x="110" y="500">一味ちがう</text>
    <text class="band-name" x="250" y="506">炭焼き月白鶏</text>
  </svg>

</main>
</body>
</html>
```